Business Card Design

I am an independent consultant to the telecommunications industry. I specialize in helping equipment manufacturers of high end fiber optic telecommunications products market and sell their products to end users such as bk&q, Quelmar, Pine Harbor Cable, Stratum 9, Dovex, etc. I conduct this activity on a global or worldwide basis. I need a professional looking card that contains a high-tech telecommunications related logo. I am thinking of something along the lines of two telephone poles separated by a bright narrow beam of light (as opposed to traditional wire) and perhaps spanning a spherical globe (world).
Target Market(s)
Engineers, Executives and Purchasing Agents for Large Keystone 700 companies
Industry/Entity Type
Telecommunications
Contact Information for Business Card
Gil Harvey, President, Upland Signal Associates, LLC, 4826-Mercer Drive, Pilot Point, TX 76490-2817, 972-555-0148

```html
<!DOCTYPE html>
<html lang="en">
<head>
<meta charset="utf-8">
<title>Gil Harvey – Upland Signal Associates</title>
<link rel="stylesheet" href="https://fonts.googleapis.com/css2?family=Arimo:ital,wght@0,400;0,700;1,400&display=swap">
<style>
  :root {
    --card-bg: #ffffff;
    --card-edge: #d8312b;
    --band-blue: #0091d9;
    --name-white: #ffffff;
    --info-grey: #4b5c60;
    --mark-teal: #1f8a8c;
    --swirl-blue: #1f97dc;
    --swirl-fade: rgba(255,255,255,0);
  }
  * { margin: 0; padding: 0; box-sizing: border-box; }
  html, body {
    width: 1200px;
    height: 695px;
    overflow: hidden;
    background: var(--card-bg);
  }
  .card {
    position: relative;
    width: 1200px;
    height: 695px;
    background: var(--card-bg);
    border: 1.5px solid var(--card-edge);
    font-family: "Arimo", Arial, sans-serif;
    overflow: hidden;
  }
  .card__wash {
    position: absolute;
    left: 0;
    top: 391px;
    width: 725px;
    height: 304px;
    background: linear-gradient(90deg, var(--swirl-blue) 0%, rgba(31,151,220,0.35) 40%, var(--swirl-fade) 100%);
    opacity: 0.55;
  }
  .card__band {
    position: absolute;
    left: 0;
    top: 166px;
    width: 704px;
    height: 225px;
    background: var(--band-blue);
    color: var(--name-white);
    text-align: center;
  }
  .card__name {
    position: absolute;
    left: 0;
    width: 714px;
    top: 74px;
    font-weight: 700;
    font-size: 74px;
    line-height: 1;
  }
  .card__title {
    position: absolute;
    left: 0;
    width: 714px;
    top: 164px;
    font-style: italic;
    font-weight: 400;
    font-size: 43px;
    line-height: 1;
  }
  .brand {
    position: absolute;
    left: 815px;
    top: 120px;
    width: 310px;
    text-align: center;
  }
  .brand__dot {
    display: block;
    width: 170px;
    height: 170px;
    margin: 0 auto 22px;
    border-radius: 50%;
    background: var(--mark-teal);
  }
  .brand__name {
    font-weight: 700;
    font-size: 34px;
    color: var(--mark-teal);
    line-height: 1;
  }
  .contact {
    position: absolute;
    left: 260px;
    width: 800px;
    top: 483px;
    text-align: center;
    color: var(--info-grey);
    font-weight: 700;
    font-size: 42px;
    line-height: 55px;
    font-style: normal;
  }
</style>
</head>
<body>
  <div class="card">
    <div class="card__wash" role="img" aria-label="Soft blue decorative sweep"></div>

    <div class="card__band">
      <div class="card__name">Gil Harvey</div>
      <div class="card__title">President</div>
    </div>

    <div class="brand">
      <span class="brand__dot"></span>
      <div class="brand__name">Upland Signal</div>
    </div>

    <address class="contact">
      Upland Signal Associates, LLC<br>
      4826-Mercer Drive, Brenwick<br>
      TX 76490-2817, 355-555-0148
    </address>
  </div>
</body>
</html>
```